We are a church and would like a flyer for a special service that is held once a quarter to get families and friends to come out to join us. See below content and details for sizes.
Church Name: Covenant Harvest Global Fellowship
Church Logo : Attached
Title : Family and Friends Day
Subtitle: Strengthening Families - Connecting Relationships
Host: Bishop Kwame Dantor (file attached. Don't need full body. Please crop)
Date: Sunday, 24 May
Time: 9:30 AM
Address: 2917 Marlow Lane, Suite F, Bowie MD, 20716
Phone : 240 593 2186
Website: www.chgfellowship.org
Flyer Size: Facebook size 851 x 314 pixels, Flash size 680 x 340 & Power Point size Standard

```html
<!DOCTYPE html>
<html lang="en">
<head>
<meta charset="utf-8">
<title>Family and Friends Day – Covenant Harvest Global Fellowship</title>
<link href="https://fonts.googleapis.com/css2?family=Libre+Baskerville:wght@400;700&display=swap" rel="stylesheet">
<style>
  :root {
    --parchment-light: #ebe4d0;
    --parchment-mid: #d2c7a8;
    --parchment-edge: #948868;
    --ink-blue: #1e4f8c;
    --ink-navy: #17416f;
    --suit-light: #8d8880;
    --suit-dark: #5c5750;
    --shirt-tone: #c99a6e;
  }
  html, body {
    margin: 0;
    padding: 0;
    width: 1200px;
    height: 900px;
    overflow: hidden;
    background: #ffffff;
  }
  .flyer {
    position: relative;
    width: 1200px;
    height: 900px;
    overflow: hidden;
    font-family: "Libre Baskerville", Georgia, serif;
    color: var(--ink-blue);
    background:
      radial-gradient(ellipse 70% 65% at 62% 48%, var(--parchment-light) 0%, var(--parchment-mid) 62%, var(--parchment-edge) 100%);
  }
  .host-portrait {
    position: absolute;
    left: 14px;
    top: 0;
    width: 500px;
    height: 900px;
    border-radius: 0 0 6px 6px;
    background:
      linear-gradient(180deg, rgba(201,154,110,0.35) 0%, rgba(201,154,110,0) 40%),
      linear-gradient(100deg, var(--suit-light) 0%, var(--suit-dark) 55%, var(--suit-light) 100%);
    box-shadow: 18px 0 40px rgba(92,87,80,0.35);
  }
  .church-name {
    position: absolute;
    left: 600px;
    top: 105px;
    width: 500px;
    text-align: center;
    font-size: 30px;
    font-weight: 700;
    line-height: 1.3;
    color: var(--ink-navy);
    display: flex;
    align-items: center;
    justify-content: center;
    gap: 18px;
  }
  .church-name .mark {
    width: 26px;
    height: 26px;
    border-radius: 50%;
    background: var(--ink-navy);
    flex: none;
  }
  .title {
    position: absolute;
    left: 530px;
    width: 670px;
    top: 294px;
    margin: 0;
    text-align: center;
    font-size: 46px;
    font-weight: 400;
    letter-spacing: 1px;
    white-space: nowrap;
    color: var(--ink-blue);
  }
  .subtitle {
    position: absolute;
    left: 530px;
    width: 670px;
    top: 368px;
    margin: 0;
    text-align: center;
    font-size: 17px;
    font-weight: 700;
    letter-spacing: 0.3px;
    color: var(--ink-blue);
  }
  .details {
    position: absolute;
    left: 548px;
    top: 460px;
    margin: 0;
    padding: 0;
    list-style: none;
    font-size: 24px;
    font-weight: 700;
    color: var(--ink-blue);
  }
  .details li { height: 74px; }
  .contact {
    position: absolute;
    top: 684px;
    font-size: 16.5px;
    font-weight: 700;
    line-height: 24px;
    color: var(--ink-blue);
  }
  .contact.address { left: 548px; }
  .contact.phone { left: 914px; }
  .website {
    position: absolute;
    left: 530px;
    width: 670px;
    top: 756px;
    text-align: center;
    font-size: 16.5px;
    font-weight: 700;
    color: var(--ink-blue);
  }
</style>
</head>
<body>
  <main class="flyer">
    <div class="host-portrait" role="img" aria-label="Photo of host Bishop Kwame Dantor standing in a grey suit and peach shirt"></div>

    <div class="church-name"><span class="mark"></span><span>Covenant Harvest<br>Global Fellowship</span></div>

    <h1 class="title">Family and Friends Day</h1>
    <p class="subtitle">Strengthening Families - Connecting Relationships</p>

    <ul class="details">
      <li>-Host: Bishop Kwame Dantor</li>
      <li>-Date: Sunday, 24 May</li>
      <li>-Time: 9:30 AM</li>
    </ul>

    <div class="contact address">Address: 2917 Marlow Lane,<br>Suite F, Bowie MD, 20716</div>
    <div class="contact phone">Phone : 240 593 2186</div>

    <div class="website">www.chgfellowship.org</div>
  </main>
</body>
</html>
```